Join Our Real Estate Team

I would like to purchase a customized version of a design you have previously submitted - https://www.plumvexa.com/design/61937042

I want to create a recruitment AD. I have attached a AD I have created and would like as much of this information on an AD as possible. My main GOAL is to promote $350 Flat Fee (Includes E&O) per Transaction & No Monthly Fees.
I like to use a photo stock as I have in the attachment of various people.
I DON'T want to say "Wanted". Prefer to say something like "STOP Paying High Splits...Keep Most of YOUR hard earned Commissions"
Feel free to use other formats that might fit all the information that I have in my flyer I have uploaded.

Target Market(s)

Realtors

Industry/Entity Type

Real Estate

Font styles to use
Serif

Colors
0094D4
00A9DD
6FCCEA
C7EBF8
E9F6FB

Requirements
Must have
• See uploaded flyer to get must haves
Nice to have
• See uploaded flyer to get ideas
Should not have
• Do not want it to say "wanted"

```html
<!DOCTYPE html>
<html lang="en">
<head>
<meta charset="utf-8">
<title>Brightwater Realty Partners – Recruitment Ad</title>
<link href="https://fonts.googleapis.com/css2?family=Open+Sans:wght@400;600;700;800&display=swap" rel="stylesheet">
<style>
  :root{
    --teal:#5bc4cb;
    --teal-dark:#3fb3bb;
    --slate:#58595b;
    --ink:#3d3e40;
    --grey-text:#5f6062;
    --white:#ffffff;
    --photo-a:#cfd6dc;
    --photo-b:#8f9aa3;
  }
  *{box-sizing:border-box;margin:0;padding:0}
  html,body{width:1200px;height:1194px;overflow:hidden;background:var(--white)}
  body{font-family:'Open Sans',sans-serif;position:relative}
  .ad{position:absolute;inset:0;width:1200px;height:1194px;background:var(--white)}
  .team-photo{position:absolute;left:0;top:0;width:1200px;height:478px;
    background:linear-gradient(180deg,var(--photo-a) 0%,#b3bcc4 45%,var(--photo-b) 100%)}
  .brand-box{position:absolute;left:16px;top:0;width:274px;height:190px;background:var(--white);
    display:flex;flex-direction:column;align-items:center;justify-content:center;gap:12px}
  .brand-mark{width:22px;height:22px;border-radius:50%;background:var(--teal)}
  .brand-name{font-weight:700;font-size:22px;color:var(--ink);text-align:center;line-height:1.25}
  .pitch-band{position:absolute;left:0;top:478px;width:1200px;height:216px;background:var(--teal);text-align:center}
  .pitch-question{position:absolute;top:30px;width:100%;font-weight:700;font-size:26px;color:var(--white)}
  .pitch-headline{position:absolute;top:80px;width:100%;font-weight:700;font-size:41px;line-height:62px;letter-spacing:.5px}
  .pitch-headline .line-1{display:block;color:var(--ink)}
  .pitch-headline .line-2{display:block;color:var(--white)}
  .offer-panel{position:absolute;left:42px;top:694px;width:1124px;height:262px;background:var(--slate);
    border-radius:0 0 26px 26px}
  .offer{position:absolute;display:flex;gap:14px}
  .offer svg{flex:none;margin-top:8px}
  .offer h3{font-weight:600;font-size:35px;line-height:40px;color:var(--teal)}
  .offer h3.small{font-size:27px;line-height:34px}
  .offer p{font-size:24px;line-height:31px;color:var(--white)}
  .offer-fee{left:50px;top:40px}
  .offer-example{left:522px;top:40px}
  .offer-transaction{left:50px;top:166px}
  .offer-team{left:522px;top:166px}
  .call-label{position:absolute;left:50px;width:491px;top:982px;text-align:center;font-weight:700;font-size:32px;color:var(--grey-text)}
  .phone-pill{position:absolute;left:50px;top:1033px;width:491px;height:78px;border-radius:39px;
    background:var(--teal);border:4px solid #d7eff1;display:flex;align-items:center;justify-content:center;
    font-weight:600;font-size:54px;color:var(--white);letter-spacing:1px;box-shadow:0 10px 12px -8px rgba(0,0,0,.35)}
  .web{position:absolute;left:40px;top:1122px;display:flex;align-items:center;gap:12px;font-weight:700;font-size:27px;color:var(--teal-dark)}
  .divider{position:absolute;left:598px;top:1006px;width:3px;height:108px;background:#bdbdbd}
  .email-note{position:absolute;left:628px;top:1022px;font-size:29px;color:var(--grey-text)}
  .email{position:absolute;left:628px;top:1064px;font-weight:700;font-size:29px;color:var(--ink)}
  .address{position:absolute;left:595px;top:1124px;display:flex;align-items:center;gap:16px;font-size:25px;color:var(--grey-text)}
  .footer-bar{position:absolute;left:0;bottom:0;width:1200px;height:18px;background:var(--teal)}
</style>
</head>
<body>
<main class="ad">
  <div class="team-photo" role="img" aria-label="Stock photo of a smiling group of diverse real estate professionals in business attire, arms crossed"></div>
  <div class="brand-box">
    <span class="brand-mark"></span>
    <span class="brand-name">BRIGHTWATER<br>REALTY PARTNERS</span>
  </div>

  <section class="pitch-band">
    <p class="pitch-question">Are you frustrated giving up 20%, 30% or even 50% of your commision ???</p>
    <h1 class="pitch-headline">
      <span class="line-1">STOP PAYING HIGH SPLITS...</span>
      <span class="line-2">KEEP MOST OF YOUR HARD EARNED COMMISSIONS</span>
    </h1>
  </section>

  <section class="offer-panel">
    <div class="offer offer-fee">
      <svg width="28" height="28" viewBox="0 0 28 28"><circle cx="14" cy="14" r="14" fill="#5bc4cb"/><path d="M8 14.5l4 4 8-8" stroke="#fff" stroke-width="3" fill="none"/></svg>
      <div><h3>$350 FLAT FEE</h3><p>Includes E&amp;</p></div>
    </div>
    <div class="offer offer-example">
      <svg width="28" height="28" viewBox="0 0 28 28"><circle cx="14" cy="14" r="14" fill="#5bc4cb"/><path d="M8 14.5l4 4 8-8" stroke="#fff" stroke-width="3" fill="none"/></svg>
      <div><h3 class="small">ON A $250,000 SALE W/3% COMMISION</h3><p>$350 • Flat Fee&nbsp;&nbsp;$ 7,150<br>Commision Earned w/BWRP</p></div>
    </div>
    <div class="offer offer-transaction">
      <svg width="28" height="28" viewBox="0 0 28 28"><circle cx="14" cy="14" r="14" fill="#5bc4cb"/><path d="M8 14.5l4 4 8-8" stroke="#fff" stroke-width="3" fill="none"/></svg>
      <div><h3>PER TRANSACTION</h3><p>No Monthly Fees Timely Payouts</p></div>
    </div>
    <div class="offer offer-team">
      <svg width="28" height="28" viewBox="0 0 28 28"><circle cx="14" cy="14" r="14" fill="#5bc4cb"/><path d="M8 14.5l4 4 8-8" stroke="#fff" stroke-width="3" fill="none"/></svg>
      <div><h3>JOIN OUR TEAM</h3><p>Start Earning More Today</p></div>
    </div>
  </section>

  <p class="call-label">CALL US TODAY AT</p>
  <div class="phone-pill">555 014 2280</div>
  <p class="web">
    <svg width="24" height="24" viewBox="0 0 24 24" fill="none" stroke="#3fb3bb" stroke-width="2"><circle cx="12" cy="12" r="10"/><ellipse cx="12" cy="12" rx="4.5" ry="10"/><path d="M2 12h20M4 7h16M4 17h16"/></svg>
    www.BrightwaterRP.com
  </p>

  <div class="divider"></div>
  <p class="email-note">or email us for more information at</p>
  <p class="email">Dana@BrightwaterRP.com</p>
  <p class="address">
    <svg width="22" height="28" viewBox="0 0 22 28"><path d="M11 0C5 0 0 4.8 0 10.7 0 18 11 28 11 28s11-10 11-17.3C22 4.8 17 0 11 0z" fill="#5bc4cb"/><circle cx="11" cy="10.5" r="4" fill="#fff"/></svg>
    1280 Coral Tern Ln, Harbor Vale, FL 30417
  </p>

  <div class="footer-bar"></div>
</main>
</body>
</html>
```